Executive Taxi firm with Chauffeur service Website

I have my domain name registered and I have started to work on my site but I am struggling. I am just about to get a logo for the company and need a web site that clearly represents the fact we are an executive/luxury brand in private hire vehicles. We offer airport transfers, train station transfers, seaport transfers, holiday transfers and business to business pick up and drop off.

Target Market(s)

Corporate people, holidaymakers looking for a luxury start their holiday. VIPs' and celebrities.

Number of Pages Required

5+ page

Font styles to use
Serif
Sans Serif
Decorative
Script

Colors

Designer to choose colors to be used in the design.

Requirements
Must have
• Home Page, Services, About Us, VIP and Contact us
• Please see www.brookvane.co.uk I have started it but not happy with it at all.
Nice to have
• Booking form or enquiry form.

```html
<!DOCTYPE html>
<html lang="en">
<head>
<meta charset="utf-8">
<title>Brookvane – Executive Chauffeur Service</title>
<link href="https://fonts.googleapis.com/css2?family=Montserrat:ital,wght@0,400;0,500;0,600;0,700;1,400&family=Open+Sans:ital,wght@0,400;0,600;1,400&display=swap" rel="stylesheet">
<style>
:root{
  --blue:#1a9fd8;
  --blue-band:#2a9fd6;
  --yellow:#f2c90a;
  --ink:#1d1d1d;
  --muted:#5b5f63;
  --card-bg:#e6f1fa;
  --line:#d6d9dc;
  --footer:#050505;
  --footer-bar:#232323;
  --white:#ffffff;
}
*{box-sizing:border-box;margin:0;padding:0}
html,body{width:756px;height:1200px;overflow:hidden;background:var(--white)}
body{position:relative;font-family:"Open Sans",Arial,sans-serif;color:var(--ink)}
.abs{position:absolute}
.brand{display:flex;align-items:center;gap:6px;font-family:"Montserrat",sans-serif;font-weight:700;letter-spacing:.5px}
.brand-dot{width:18px;height:18px;border-radius:50%;background:var(--blue)}

/* header */
.site-header{left:0;top:0;width:756px;height:45px;background:var(--white)}
.site-header .brand{position:absolute;left:80px;top:11px;font-size:17px;color:var(--ink)}
.main-nav{position:absolute;top:17px;left:0;font-family:"Montserrat",sans-serif;font-size:8.5px;font-weight:500;color:var(--ink)}
.main-nav span{position:absolute;white-space:nowrap}
.main-nav .active{border-bottom:1.5px solid var(--blue);padding-bottom:3px}
.header-phone{position:absolute;left:570px;top:13px;display:flex;align-items:center;gap:6px;font-family:"Montserrat",sans-serif;font-size:11.5px;font-weight:500}
.phone-icon{width:18px;height:18px;border-radius:50%;background:var(--yellow);display:flex;align-items:center;justify-content:center}

/* hero */
.hero{left:0;top:45px;width:756px;height:273px;background:linear-gradient(100deg,#3d3f40 0%,#6c6a5e 25%,#8a7a3c 38%,#55534d 55%,#9a9a98 75%,#c9c9c7 100%)}
.hero-title{left:81px;top:172px;font-family:"Montserrat",sans-serif;font-size:20.5px;font-weight:500;color:var(--white)}
.hero-sub{left:81px;top:199px;font-family:"Montserrat",sans-serif;font-size:13px;color:var(--white)}

.booking{left:407px;top:92px;width:267px;height:183px;background:var(--white)}
.booking-head{height:32px;background:var(--blue);color:var(--white);font-family:"Montserrat",sans-serif;font-size:12.5px;font-weight:500;text-align:center;line-height:32px;letter-spacing:.3px}
.field{position:absolute;width:120px;height:24px;border:1px solid #c9cdd0;font-size:8px;color:#444;padding-left:9px;line-height:22px}
.field .caret{position:absolute;right:8px;top:0;font-size:7px;color:#666}
.submit{position:absolute;left:11px;top:141px;width:246px;height:27px;background:var(--yellow);font-family:"Montserrat",sans-serif;font-weight:600;font-size:12px;text-align:center;line-height:27px;letter-spacing:.3px}

/* stats */
.stats{left:0;top:318px;width:756px;height:63px;border-bottom:1px solid #ececec}
.stat{position:absolute;width:120px;margin-left:-60px;text-align:center;top:18px}
.stat b{display:block;font-family:"Montserrat",sans-serif;font-weight:500;font-size:12px;color:var(--blue)}
.stat small{display:block;font-size:8px;color:#333;margin-top:1px}
.stat-divider{position:absolute;top:22px;width:1px;height:24px;background:#e3e3e3}

/* services */
.service{position:absolute;top:396px;width:190px;height:199px;background:var(--card-bg)}
.service-photo{height:116px}
.service h3{font-family:"Montserrat",sans-serif;font-weight:500;font-size:10.5px;margin:11px 0 0 13px}
.service p{font-size:7.8px;line-height:10.8px;color:var(--muted);margin:4px 10px 0 12px}

/* heritage band */
.heritage{left:0;top:614px;width:756px;height:248px;background:linear-gradient(180deg,#2aa0d8,#2196cf)}
.heritage h2{position:absolute;top:54px;width:756px;text-align:center;font-family:"Montserrat",sans-serif;font-weight:400;font-size:19px;color:var(--white)}
.heritage h2 em{font-style:normal;color:var(--yellow)}
.heritage .copy{position:absolute;left:128px;top:82px;width:500px;text-align:center;color:var(--white);font-size:8.1px;line-height:10.8px}
.heritage .copy p{margin-bottom:10.8px}

/* testimonials */
.testimonials-title{left:0;top:880px;width:756px;text-align:center;font-family:"Montserrat",sans-serif;font-weight:500;font-size:14px}
.quote{position:absolute;top:917px;width:250px;height:93px;border:2px solid #e3e3e3;padding:14px 18px 0 18px}
.quote p{font-style:italic;font-size:10.3px;line-height:14px;color:#555}
.quote cite{display:block;font-style:normal;font-family:"Montserrat",sans-serif;font-weight:500;font-size:8.5px;color:var(--ink);margin-top:8px}
.dot{position:absolute;top:1021px;width:7px;height:7px;border-radius:50%;background:#c9c9c9}
.dot.on{background:#8a8a8a}

/* footer */
.site-footer{left:0;top:1046px;width:756px;height:124px;background:var(--footer);color:var(--white)}
.site-footer .brand{position:absolute;left:81px;top:22px;font-size:15px;color:var(--white)}
.contact-lines{position:absolute;left:85px;top:56px;font-family:"Montserrat",sans-serif;font-size:8.6px;line-height:13px}
.foot-col{position:absolute;top:24px}
.foot-col h4{font-family:"Montserrat",sans-serif;font-weight:500;font-size:8.8px;margin-bottom:5px}
.foot-col li{list-style:none;font-size:7.6px;line-height:13px;color:#a9a9a9}
.foot-col .note{font-size:7.6px;color:#a9a9a9}
.newsletter{position:absolute;left:1px;top:37px;width:148px;height:23px;display:flex}
.newsletter span{flex:1;background:var(--white);color:#777;font-size:7.6px;line-height:23px;padding-left:9px}
.newsletter b{width:28px;background:var(--yellow);color:var(--ink);font-family:"Montserrat",sans-serif;font-size:8.5px;font-weight:600;text-align:center;line-height:23px}
.footer-bar{left:0;top:1170px;width:756px;height:30px;background:var(--footer-bar);color:#9a9a9a;font-size:7.6px;text-align:center;line-height:30px}
</style>
</head>
<body>

<header class="abs site-header">
  <div class="brand"><span class="brand-dot"></span>BROOKVANE</div>
  <nav class="main-nav">
    <span class="active" style="left:323px">HOME</span>
    <span style="left:362px">SERVICES</span>
    <span style="left:417px">ABOUT US</span>
    <span style="left:473px">VIP</span>
    <span style="left:500px">CONTACT US</span>
  </nav>
  <div class="header-phone">
    <span class="phone-icon">
      <svg width="10" height="10" viewBox="0 0 24 24"><path fill="#1d1d1d" d="M6.6 10.8a15.1 15.1 0 0 0 6.6 6.6l2.2-2.2c.3-.3.7-.4 1-.2 1.1.4 2.3.6 3.6.6.6 0 1 .4 1 1V20c0 .6-.4 1-1 1A17 17 0 0 1 3 4c0-.6.4-1 1-1h3.5c.6 0 1 .4 1 1 0 1.3.2 2.5.6 3.6.1.3 0 .7-.2 1z"/></svg>
    </span>
    07700 900418
  </div>
</header>

<section class="abs hero" role="img" aria-label="Photo of a yellow taxi at a city kerbside with passengers getting in"></section>
<h1 class="abs hero-title">Reliable. Safe. Transparent.</h1>
<p class="abs hero-sub">Your trusted ride for every occasion!</p>

<form class="abs booking">
  <div class="booking-head">BOOK A RIDE WITH US</div>
  <div class="field" style="left:11px;top:43px">First Name</div>
  <div class="field" style="left:137px;top:43px">Last Name</div>
  <div class="field" style="left:11px;top:75px">Email Address</div>
  <div class="field" style="left:137px;top:75px">Phone Number</div>
  <div class="field" style="left:11px;top:108px">Date</div>
  <div class="field" style="left:137px;top:108px">Time<span class="caret">&#9660;</span></div>
  <div class="submit">SUBMIT</div>
</form>

<section class="abs stats">
  <div class="stat" style="left:192px"><b>36,400</b><small>Journeys to date</small></div>
  <div class="stat-divider" style="left:258px"></div>
  <div class="stat" style="left:313px"><b>02</b><small>Locations</small></div>
  <div class="stat-divider" style="left:375px"></div>
  <div class="stat" style="left:434px"><b>08</b><small>Staff</small></div>
  <div class="stat-divider" style="left:493px"></div>
  <div class="stat" style="left:556px"><b>60+</b><small>Years</small></div>
</section>

<article class="service" style="left:81px">
  <div class="service-photo" role="img" aria-label="Traveller pulling a suitcase along an airport pavement" style="background:linear-gradient(135deg,#c9c2b4,#8f877a 55%,#5a5249)"></div>
  <h3>Airport Transfers</h3>
  <p>Airport and Seaport transfers are a particular speciality of ours. We have in depth knowledge of the road network around all major airports and seaports alike.</p>
</article>
<article class="service" style="left:283px">
  <div class="service-photo" role="img" aria-label="Businessman in a suit stepping out of a car" style="background:linear-gradient(135deg,#dfe3e6,#9aa3ab 55%,#4f565d)"></div>
  <h3>Business to Business Transfers</h3>
  <p>If its a stress free chauffeur service you need then look no further. A selection of vehicles to choose from that all come with full leather and air conditioning.</p>
</article>
<article class="service" style="left:485px">
  <div class="service-photo" role="img" aria-label="Passenger relaxing with headphones in the back of a car" style="background:linear-gradient(135deg,#c7a56b,#6b6257 50%,#2e3a4a)"></div>
  <h3>Holiday Transfers</h3>
  <p>Why not start your holiday off stress free and allow us to take care of your outbound and return journey to and from the airport, seaport or train station.</p>
</article>

<section class="abs heritage" role="img" aria-label="Blue-tinted view from inside a car in city traffic">
  <h2>We've been in the transport industry for over <em>60 years</em></h2>
  <div class="copy">
    <p>That’s 60 years of history and business ‘know how’.<br>Being one of the very first car transporters in the area we have now changed our expertise to transporting people throughout the UK and Europe.</p>
    <p>Our fleet of SUVs, Cars and Transporters are all top of the range latest models, boasting leather interior, A/C front and rear, ample boot space which means our customers benefit from the very finest in luxury land travel.</p>
    <p>We will continue to invest in our fleet to ensure our drivers and customers benefit fully from all that modern information and technology has to offer, without losing that personal touch. We offer the very best services in our field. We never settle for second best, and always have your satisfaction as our top priority. It’s who we are, and we are proud of it.</p>
  </div>
</section>

<h2 class="abs testimonials-title">Satisfied Customers</h2>
<blockquote class="quote" style="left:122px">
  <p>“Having used so many different taxi firms over the years these guys really know how to look after you. A reall touch of class to your journey.”</p>
  <cite>Mark Ellison, MD Coventry</cite>
</blockquote>
<blockquote class="quote" style="left:382px">
  <p>“This is the best company I have ever worked with. I’ll definitely choose them again, and highly recommend them.”</p>
  <cite>Dana Wells, Ops Director Birmingham</cite>
</blockquote>
<span class="dot on" style="left:361px"></span>
<span class="dot" style="left:373px"></span>
<span class="dot" style="left:385px"></span>

<footer class="abs site-footer">
  <div class="brand"><span class="brand-dot"></span>BROOKVANE</div>
  <div class="contact-lines">07700 900418<br>info@brookvane.co.uk</div>
  <div class="foot-col" style="left:238px">
    <h4>Quick Links</h4>
    <ul><li>Home</li><li>Services</li><li>About</li><li>VIP</li><li>Contact</li></ul>
  </div>
  <div class="foot-col" style="left:370px">
    <h4>Services</h4>
    <ul><li>Airport Transfers</li><li>Business to Business Transfers</li><li>Holiday Transfers</li></ul>
  </div>
  <div class="foot-col" style="left:525px">
    <h4>Stay Connected</h4>
    <p class="note">Join our newsletter and find out more.</p>
    <div class="newsletter"><span>Email</span><b>GO</b></div>
  </div>
</footer>
<div class="abs footer-bar">© 2018 brookvane. All Rights Reserved</div>

</body>
</html>
```